Website ui design required!

I require a web page ui design.
Theme: Outsourcing platform for developers and clients.
This website will be specifically for app/android/game/windows developers.
Anything that can be outsourced for app categories.
*App solutions
*Graphic design
*Marketing
*Project management
*mobile
*sdk intergration
*Developers
Basically if you want an app built on any platform, this website allows clients to connect with developers and other services surrounding that environment.
Please look at www.briskwork.com.au
Www.plorvin.com
Www.tefa.com
www.vormix.com
www.pellowind.com
Please make it look sleek and appealing.
I want this website to be the no.1 place for clients to source the best app developers worldwide. (random) I noticed these websites are 2 toned in color split, top and bottom.
All the best!!:)
Please take a look at the websites I mentioned.
Target Market(s)
Target market will be for anyone who wishes to
Find a developer, graphic artist, mobile apps, sdk integration,
app design, app consultation, web/mobile project management etc.
This is going to be an outsourcing platform for developers worldwide, also a place
For clients to hire manage and pay developers.
Industry/Entity Type
Graphic Design
Look and feel
Each slider illustrates characteristics of the customer's brand and the style your logo design should communicate.

```html
<!DOCTYPE html>
<html lang="en">
<head>
<meta charset="utf-8">
<title>NODE7 — App Development in 3 Steps</title>
<link rel="stylesheet" href="https://fonts.googleapis.com/css2?family=Oswald:wght@300;400&family=Arimo:wght@400;700&display=swap">
<style>
  :root {
    --ink: #2e2e2e;
    --black: #000;
    --accent: #0a97d0;
    --muted: #9a9a9a;
    --band: #e0e0e0;
    --header-top: #dedede;
    --white: #fff;
    --rule: #a8a8a8;
    --art-light: #efefef;
    --art-mid: #cfcfcf;
    --art-blue: #9cc3de;
  }
  * { margin: 0; padding: 0; box-sizing: border-box; }
  html, body { width: 1200px; height: 768px; overflow: hidden; }
  body {
    position: relative;
    font-family: "Arimo", Arial, sans-serif;
    color: var(--ink);
    background: radial-gradient(ellipse 520px 260px at 600px 470px, #fdfdfd 0%, #f4f4f4 55%, var(--band) 100%);
  }
  .utility-bar {
    position: absolute; top: 0; left: 0; width: 1200px; height: 21px;
    background: var(--white); border-bottom: 2px solid var(--accent);
  }
  .audience-tabs { position: absolute; left: 178px; top: 0; display: flex; }
  .audience-tab {
    height: 22px; padding: 0 9px; font: 400 13px/22px "Oswald", sans-serif;
    border: 1px solid #ccc; border-top: none; background: linear-gradient(#fff, #ececec);
    text-transform: uppercase;
  }
  .audience-tab.is-active { color: var(--ink); }
  .audience-tab.is-inactive { color: var(--muted); }
  .account-links {
    position: absolute; right: 164px; top: 0; height: 22px; padding: 0 11px;
    font: 300 13px/22px "Oswald", sans-serif; border: 1px solid #ccc; border-top: none;
    background: linear-gradient(#fff, #ececec); text-transform: uppercase;
  }
  .account-links b { font-weight: 400; margin: 0 4px; }
  .site-header {
    position: absolute; top: 23px; left: 0; width: 1200px; height: 96px;
    background: linear-gradient(var(--header-top), #f7f7f7 60%, var(--white));
  }
  .brand {
    position: absolute; left: 176px; top: 14px;
    font: 300 56px/1 "Oswald", sans-serif; color: var(--black); letter-spacing: -1px;
  }
  .main-nav { position: absolute; left: 351px; top: 38px; display: flex; font-size: 13px; color: var(--black); }
  .main-nav span { display: inline-block; }
  .main-nav .is-current { font-weight: 700; }
  .main-nav .dot { margin: 0 19px; }
  .steps-band {
    position: absolute; top: 119px; left: 0; width: 1200px; height: 212px; background: var(--band);
  }
  .headline {
    position: absolute; top: 162px; left: 0; width: 1200px; text-align: center;
    font: 400 37px/1 "Oswald", sans-serif; color: var(--ink); letter-spacing: 0.5px;
  }
  .headline .step-count {
    display: inline-block; width: 32px; height: 32px; margin: 0 12px; border-radius: 50%;
    background: var(--accent); color: var(--white); font-size: 26px; line-height: 32px; vertical-align: 3px;
  }
  .subheadline {
    position: absolute; top: 203px; left: 0; width: 1200px; text-align: center;
    font-size: 15px; letter-spacing: 0.6px;
  }
  .step-card {
    position: absolute; top: 273px; width: 261px; height: 68px;
    background: linear-gradient(#d8d8d8, #f4f4f4); border: 1px solid #c8c8c8;
    box-shadow: 4px 3px 5px rgba(0,0,0,0.15);
    font: 400 30px/64px "Oswald", sans-serif; text-align: center; color: var(--ink);
  }
  .step-card::after {
    content: ""; position: absolute; left: 0; right: 0; bottom: 0; height: 8px; background: var(--accent);
  }
  .step-art { position: absolute; border-radius: 4px; }
  .art-form { left: 262px; top: 372px; width: 88px; height: 96px; background: linear-gradient(var(--art-light), #e2e2e2); }
  .art-laptop { left: 512px; top: 367px; width: 195px; height: 113px; background: linear-gradient(var(--art-light), var(--art-mid)); }
  .art-developer { left: 814px; top: 363px; width: 133px; height: 125px; background: linear-gradient(var(--art-blue), var(--art-mid)); }
  .cta-title {
    position: absolute; left: 271px; top: 560px;
    font: 400 31px/1 "Oswald", sans-serif; color: var(--accent); letter-spacing: 0.3px;
  }
  .cta-title strong { font-weight: 400; color: var(--black); }
  .cta-note { position: absolute; right: 483px; top: 592px; font-size: 14px; color: var(--ink); }
  .cta-button {
    position: absolute; left: 731px; top: 563px; width: 211px; height: 42px;
    background: var(--black); color: var(--white); font: 700 16px/42px "Arimo", sans-serif;
    text-align: center; letter-spacing: -0.3px;
  }
  .footer-rule { position: absolute; left: 178px; top: 652px; width: 858px; height: 1px; background: var(--rule); }
  .footer-nav { position: absolute; top: 692px; left: 0; width: 1200px; text-align: center; font-size: 12px; letter-spacing: 0.4px; }
  .footer-nav .sep { margin: 0 11px; }
  .copyright { position: absolute; top: 721px; left: 0; width: 1200px; text-align: center; font-size: 12px; letter-spacing: 0.4px; }
</style>
</head>
<body>
  <div class="utility-bar">
    <nav class="audience-tabs">
      <span class="audience-tab is-active">Employers</span>
      <span class="audience-tab is-inactive">App Developers</span>
    </nav>
    <div class="account-links">Login <b>or</b> Join Now</div>
  </div>

  <header class="site-header">
    <div class="brand">NODE7</div>
    <nav class="main-nav">
      <span class="is-current">Home</span><span class="dot">•</span>
      <span>How it Works</span><span class="dot">•</span>
      <span>Hire Developer</span><span class="dot">•</span>
      <span>Find Work</span><span class="dot">•</span>
      <span>FAQs</span><span class="dot">•</span>
      <span>Contact Us</span>
    </nav>
  </header>

  <div class="steps-band"></div>
  <h1 class="headline">APP DEVELOPMENT IN<span class="step-count">3</span>STEPS</h1>
  <p class="subheadline">Mob App Developers on Demand!</p>

  <div class="step-card" style="left:178px">SIGN UP</div>
  <div class="step-card" style="left:477px">POST A JOB</div>
  <div class="step-card" style="left:775px">HIRE DEVELOPER</div>

  <div class="step-art art-form" role="img" aria-label="Illustration of a sign-up form with a fountain pen"></div>
  <div class="step-art art-laptop" role="img" aria-label="Illustration of a laptop showing the job posting page"></div>
  <div class="step-art art-developer" role="img" aria-label="Illustration of a developer in a suit beside a globe"></div>

  <h2 class="cta-title">POSTING A PROJECT IS EASY AND <strong>FREE!</strong></h2>
  <p class="cta-note">Register Now And make transctions instantly</p>
  <div class="cta-button">POST PROJECT NOW</div>

  <div class="footer-rule"></div>
  <nav class="footer-nav">
    Home<span class="sep">I</span>How it Works<span class="sep">I</span>Hire Developer<span class="sep">I</span>Find a work<span class="sep">I</span>FAQs<span class="sep">I</span>Contact Us
  </nav>
  <p class="copyright">Node7.com © 2013 · All rights reserved.</p>
</body>
</html>
```